Tolvene Hub Redesign

tolvenehub.com is one of our old, high-traffic multilingual site.

its interface is very old, so we want to redesign it to give a modern, attractive design, with comfortable colors and layout.

beside the current content of the main page we want to add two places for dynamic banners.

The site has an App in iOS and Android, we want an ad in a noticeable place for it.

this ad will be permanent.

the site now has 12 languages, but we may add new languages soon, so design must consider this.

redesign of two internal pages also required:
- the main listing page, example: http://www.tolvenehub.example/en/cat/252
- the article view page: http://www.tolvenehub.example/en/10323

Reason: want to receive more designs ...

```html
<!DOCTYPE html>
<html lang="en">
<head>
<meta charset="utf-8">
<title>Tolvene Hub</title>
<link href="https://fonts.googleapis.com/css2?family=Roboto:wght@400;500&family=Oswald:wght@400;500&display=swap" rel="stylesheet">
<style>
:root{
  --orange:#ee9a10;
  --orange-dark:#d0520f;
  --rust:#b5371a;
  --brown:#8a3b0a;
  --yellow:#f7c600;
  --text:#444;
  --line:#d8d8d8;
  --panel:#f4f4f4;
  --footer:#464646;
}
*{box-sizing:border-box;margin:0;padding:0}
html,body{width:973px;height:1200px;overflow:hidden;background:#fff}
body{font-family:Roboto,sans-serif;color:var(--text)}
.page{position:relative;width:1200px;height:1480px;transform:scale(0.81083);transform-origin:0 0}
.abs{position:absolute}
ul{list-style:none}

.topbar{left:0;top:0;width:1200px;height:50px;background:var(--orange)}
.date{left:130px;top:16px;color:#fff;font-size:13px;letter-spacing:.3px}
.search{left:621px;top:10px;width:255px;height:30px;background:#fff;font-size:12px;font-style:italic;color:#999;padding:9px 13px}
.search-btn{left:876px;top:10px;width:42px;height:30px;background:var(--yellow)}
.lang{left:930px;top:9px;width:140px;height:30px;background:#fff;font-size:13px;color:#444;padding:8px 0 0 47px}
.lang .flag{position:absolute;left:10px;top:8px;width:24px;height:15px;background:#2a3f8f}
.lang .caret{position:absolute;right:8px;top:12px}

.header{left:0;top:50px;width:1200px;height:85px;background:linear-gradient(180deg,#a3290a 0%,#d0520f 50%,#9c2608 100%)}
.brand{left:135px;top:62px;color:#fff}
.brand-name{font-size:44px;font-weight:400;line-height:1;letter-spacing:.5px}
.brand-tag{font-size:11px;letter-spacing:1.5px;margin-top:6px;margin-left:40px}
.top-ad{left:450px;top:53px;width:622px;height:77px;background:linear-gradient(90deg,#fff 0%,#6cbf3f 25%,#3f9b2a 60%,#f3d9c4 100%);border:1px solid #ccc}

.nav{left:0;top:135px;width:1200px;height:53px;background:linear-gradient(180deg,#c74a0e 0,#c74a0e 3px,#fde04e 4px,#f6b41a 100%)}
.nav ul{display:flex;position:absolute;left:136px;top:20px;gap:0}
.nav li{font-size:15px;color:var(--brown);margin-right:33px}
.nav li:last-child{margin-right:0}

.slider{left:130px;top:193px;width:940px;height:370px;background:#e4e4e4}
.slide{left:135px;top:198px;width:930px;height:360px;background:linear-gradient(90deg,#fff 0%,#f5f7fa 30%,#e6edf4 100%)}
.slide-photo{left:410px;top:198px;width:655px;height:360px;background:linear-gradient(180deg,#dfe8f2 0%,#c9a23e 35%,#4d6aa0 60%,#b8a88a 85%,#8a7d6a 100%);clip-path:polygon(15% 0,100% 0,100% 100%,0 100%,0 80%)}
.slide-title{left:170px;top:262px;font-family:Oswald,sans-serif;font-size:38px;line-height:43px;color:var(--rust)}
.slide-text{left:171px;top:355px;font-size:15px;line-height:20px;color:#333;letter-spacing:.2px}
.dots{left:170px;top:525px;display:flex;gap:4px}
.dots span{width:13px;height:13px;border-radius:50%;background:#777}
.dots span:first-child{background:var(--orange)}

.bullets li{position:relative;padding-left:22px;font-size:13px;line-height:20px;color:var(--text);letter-spacing:.2px}
.bullets li::before{content:"";position:absolute;left:0;top:6px;width:8px;height:8px;border-radius:50%;background:var(--orange-dark)}

.section-title{left:128px;top:584px;font-size:22px;color:var(--orange-dark);letter-spacing:.3px}
.fatwas{left:129px;top:622px;width:550px}
.fatwas li{margin-bottom:8px}
.btn{left:130px;top:882px;width:114px;height:34px;background:var(--orange);color:#fff;font-size:13px;text-align:center;line-height:34px;letter-spacing:.5px}

.tab{top:588px;height:40px;font-size:16px;text-align:center;line-height:40px;font-weight:500}
.tab-cat{left:690px;width:140px;background:linear-gradient(#fff,#f2f2f2);border:1px solid var(--line);border-bottom:none;color:var(--orange-dark)}
.tab-files{left:835px;width:74px;background:var(--orange);color:#fff}
.tab-panel{left:690px;top:628px;width:380px;height:289px;border:1px solid var(--line);background:linear-gradient(#fff,#f6f6f6)}
.cats{left:705px;top:646px}
.cats li{margin-bottom:3px}
.more{left:992px;top:887px;font-size:13px;color:var(--orange-dark)}

.acc{left:130px;width:620px;border:1px solid var(--line);background:linear-gradient(#fff,#f1f1f1)}
.acc-title{position:absolute;left:20px;top:10px;font-size:16px;color:var(--orange-dark);letter-spacing:.3px}
.acc-icon{position:absolute;right:14px;width:18px;height:18px;border-radius:50%;background:linear-gradient(#fafafa,#ccc);border:1px solid #bbb}
.acc-body{position:absolute;left:0;top:40px;width:618px;border-top:1px solid var(--line);background:var(--panel);padding:8px 0 0 20px}
.acc-body li{margin-bottom:8px;width:560px}

.side-ad{left:771px;top:937px;width:300px;height:250px;background:linear-gradient(180deg,#efefef 0,#efefef 20%,#fff 22%,#f3a23a 60%,#222 75%,#d3101a 100%);border:6px solid #6cb43f}

.apps{left:770px;top:1209px;width:300px;height:114px;border:1px solid var(--line);background:var(--panel)}
.apps-head{position:absolute;left:0;top:0;width:298px;height:38px;border-bottom:1px solid var(--line);background:linear-gradient(#fff,#f3f3f3);font-size:16px;color:#444;padding:9px 16px}
.app{position:absolute;top:50px;display:flex;align-items:center;gap:14px;font-size:14px;color:var(--orange-dark);font-weight:500}
.app .ico{width:38px;height:46px;border-radius:6px}

.footer{left:0;top:1393px;width:1200px;height:87px;background:var(--footer)}
.copy{left:129px;top:1428px;font-size:12px;color:#ddd;letter-spacing:.3px}
.copy b{font-weight:400;color:var(--orange)}
.social{top:1421px;width:30px;height:30px;border-radius:4px}
</style>
</head>
<body>
<div class="page">
  <div class="abs topbar"></div>
  <div class="abs date">Fri 27 DhH 1434 - 1 November 2013</div>
  <div class="abs search">Search...</div>
  <div class="abs search-btn">
    <svg width="42" height="30" viewBox="0 0 42 30"><circle cx="19" cy="13" r="6" fill="none" stroke="#6b3a00" stroke-width="2.5"/><line x1="23.5" y1="17.5" x2="29" y2="23" stroke="#6b3a00" stroke-width="3"/></svg>
  </div>
  <div class="abs lang"><span class="flag"></span>English
    <svg class="caret" width="14" height="8"><path d="M0 0h14L7 8z" fill="#999"/></svg>
  </div>

  <div class="abs header"></div>
  <div class="abs brand">
    <div class="brand-name">Tolvene Hub</div>
    <div class="brand-tag">QUESTION &amp; ANSWER</div>
  </div>
  <div class="abs top-ad" role="img" aria-label="Banner advert for Vantrel Cover term life insurance"></div>

  <nav class="abs nav">
    <ul>
      <li>Home</li><li>Categories</li><li>NewFatwas</li><li>About</li><li>Articles &amp; Books</li><li>Send A Question</li><li>Introduction to Islam</li><li>Contact Us</li>
    </ul>
  </nav>

  <div class="abs slider"></div>
  <div class="abs slide"></div>
  <div class="abs slide-photo" role="img" aria-label="Photo of a golden-domed mosque under a bright sky"></div>
  <h1 class="abs slide-title">Lorem ipsum dolor sit<br>amet consectetur</h1>
  <p class="abs slide-text">Vivamus egestas risus in magna varius commodo<br>Sed semper viverra egestas.</p>
  <div class="abs dots"><span></span><span></span><span></span><span></span></div>

  <h2 class="abs section-title">New Fatwas</h2>
  <ul class="abs bullets fatwas">
    <li>Ruling on offering congratulations at the beginning of the Hijri year.</li>
    <li>He works as a nurse, which means that he may do some things that are not acceptable according to sharee’ah.</li>
    <li>Her mother wants her to marry one suitor, but her father thinks that he is not suitable; what should she do?.</li>
    <li>Tawaaf (circumambulation of the Ka’bah) when one is uncertain about one’s state of purity.</li>
    <li>Raising Muslim children in the West to have an aversion to pigs.</li>
    <li>His parents think that he does not offer the naafil prayers, but he prays them in secret for fear of showing off. Should he tell them about that?.</li>
  </ul>
  <div class="abs btn">READ ALL</div>

  <div class="abs tab-panel"></div>
  <div class="abs tab tab-cat">Categories</div>
  <div class="abs tab tab-files">Files</div>
  <ul class="abs bullets cats">
    <li>Basic Tenets of Faith.</li>
    <li>The Quraan and its Sciences.</li>
    <li>Hadeeth &amp; its Sciences.</li>
    <li>Rulings on Jihaad.</li>
    <li>Fiqh of the family.</li>
    <li>Islamic history and biography.</li>
    <li>Enjoining what is good and forbidding what is evil.</li>
    <li>Pedagogy education and upbringing.</li>
    <li>Psychological and Social Problems.</li>
    <li>Islamic politics.</li>
  </ul>
  <div class="abs more">Read More</div>

  <div class="abs acc" style="top:937px;height:211px">
    <div class="acc-title">Counselling</div>
    <span class="acc-icon" style="top:12px"><svg width="16" height="16"><path d="M4 6h8l-4 5z" fill="#222"/></svg></span>
    <ul class="acc-body bullets" style="height:170px">
      <li>Her fiancé refuses to let her wear hijab.</li>
      <li>His wife torments his daughter from another wife, and he has a son from her, and he is confused as to how he should deal with her.</li>
      <li>A woman asking for a divorce from her husband who is addicted to drugs.</li>
      <li>He did the marriage contract with her and was intimate with her without intercourse in Ramadaan, and he had intercourse with her before announcing the marriage!.</li>
    </ul>
  </div>
  <div class="abs acc" style="top:1151px;height:43px"><div class="acc-title">Jurisprudence of Acts of Worship</div><span class="acc-icon" style="top:12px"><svg width="16" height="16"><path d="M6 4v8l5-4z" fill="#222"/></svg></span></div>
  <div class="abs acc" style="top:1197px;height:43px"><span class="acc-icon" style="top:12px"><svg width="16" height="16"><path d="M6 4v8l5-4z" fill="#222"/></svg></span></div>
  <div class="abs acc" style="top:1243px;height:43px"><div class="acc-title">Contemporary Transactions</div><span class="acc-icon" style="top:12px"><svg width="16" height="16"><path d="M6 4v8l5-4z" fill="#222"/></svg></span></div>
  <div class="abs acc" style="top:1289px;height:43px"><div class="acc-title">Basic Tenets of Faith</div><span class="acc-icon" style="top:12px"><svg width="16" height="16"><path d="M6 4v8l5-4z" fill="#222"/></svg></span></div>
  <div class="abs acc" style="top:1335px;height:43px"><div class="acc-title">The Muslim Woman</div><span class="acc-icon" style="top:12px"><svg width="16" height="16"><path d="M6 4v8l5-4z" fill="#222"/></svg></span></div>

  <div class="abs side-ad" role="img" aria-label="Banner advert from kermadashop.com for a Norvik Flash 4GB pen drive"></div>

  <div class="abs apps">
    <div class="apps-head">App Store</div>
    <div class="app" style="left:16px"><span class="ico" style="background:linear-gradient(#eee,#bbb)"></span>Pomme OS</div>
    <div class="app" style="left:152px"><span class="ico" style="background:linear-gradient(#a4d24a,#6aa91f)"></span>Robo OS</div>
  </div>

  <footer class="abs footer"></footer>
  <div class="abs copy">Copyright © 1997-2013 <b>Tolvene Hub</b> All Rights Reserved &nbsp;&nbsp;&nbsp;&nbsp;&nbsp;43.69</div>
  <div class="abs social" style="left:998px;background:#3b5a9a" aria-label="Share"></div>
  <div class="abs social" style="left:1041px;background:#4fb8e6" aria-label="Post"></div>
</div>
</body>
</html>
```